Compelling Home Page for Clip Harbor Partners

We are a Video SEO specialist that get websites on top of the front page of Zentrova and FlickBarn with video thumbprints that generate great traffic. Video SEO is all we do

see what we're offering at a salespage www.plumfieldreels.example. However, please omit "guarantee"

he home page should introduce our company as a premier company for helping brands get their videos on the front page of zentrova and high up in flickbarn. Should incorporate video "thumbnails" as part of the design. These could be the "triangular click buttons" or little video screens you see as "thumbnails" Needs a prominent place for a video about videoSEO. on Left side of page towards the top.

Needs buttons across the top for other pages. See www.brastonclips.example for frame of reference we want to be better than them.

Must incorporate our logo. We'd like to see the logo on dark background as well as white background.

Simple but with bright and vibrant highlights that look sophisticated, cutting edge and accountable. Shows credentials. Links with examples of thumbnails that are on the front page

We want to beat www.brastonclips.example check it out for point of reference

Target Market(s)

large corporations who have videos already and want to get better traction. Marlow 500. Advertising Agencies for Marlow 500's

Requirements
Must have
• Incorporate our logo. clean, easy to read

```html
<!DOCTYPE html>
<html lang="en">
<head>
<meta charset="utf-8">
<title>Clip Harbor Partners – Home</title>
<link href="https://fonts.googleapis.com/css2?family=Arimo:ital,wght@0,400;0,700;1,400;1,700&display=swap" rel="stylesheet">
<style>
  :root {
    --bg-deep: #04143a;
    --bg-mid: #0a2c6e;
    --bg-low: #0b4a6e;
    --ink-white: #ffffff;
    --ink-black: #000000;
    --ink-grey: #8a8f96;
    --panel-light: #e9eef3;
    --panel-navy: #061544;
    --frame-silver: #b9bcc0;
    --screen-white: #ffffff;
    --play-yellow: #fbf59c;
    --accent-blue: #1d7fe0;
    --link-blue: #3d8fe3;
    --footer-ink: #b9c9d8;
    --pill-dark: #111418;
  }
  * { box-sizing: border-box; margin: 0; padding: 0; }
  html, body { width: 1200px; height: 900px; overflow: hidden; }
  body {
    position: relative;
    font-family: "Arimo", Arial, sans-serif;
    background:
      radial-gradient(ellipse 420px 300px at 170px 70px, #1a4fa8 0%, rgba(10,44,110,0) 70%),
      linear-gradient(180deg, var(--bg-deep) 0%, var(--bg-mid) 30%, #0a2f66 60%, var(--bg-low) 100%);
    color: var(--ink-white);
  }
  .abs { position: absolute; }

  .tagline {
    left: 566px; top: 7px; width: 540px;
    font-style: italic; font-size: 15px; line-height: 17.5px;
  }

  .brand { left: 122px; top: 22px; display: flex; align-items: center; gap: 14px; }
  .brand-dot {
    width: 96px; height: 96px; border-radius: 50%;
    background: var(--accent-blue);
  }
  .brand-name { font-size: 34px; font-weight: 400; color: var(--ink-white); letter-spacing: -0.5px; }

  .main-nav { left: 508px; top: 145px; display: flex; gap: 3px; }
  .nav-btn {
    width: 116px; height: 50px; border-radius: 25px;
    background: linear-gradient(180deg, #3a4048 0%, var(--pill-dark) 45%, #000 100%);
    box-shadow: 0 0 0 3px #1b5fd0, 0 0 8px #2b7cff;
    display: flex; align-items: center; gap: 6px; padding-left: 10px;
    color: var(--ink-white); font-size: 15px; text-decoration: none;
  }
  .nav-btn svg { flex: none; }

  .hero-panel {
    left: 108px; top: 200px; width: 986px; height: 238px;
    background: linear-gradient(180deg, #f6f8fa 0%, var(--panel-light) 100%);
    border-radius: 18px;
  }
  .hero-curl { left: 1046px; top: 393px; }

  .video-frame {
    left: 120px; top: 163px; width: 382px; height: 262px;
    border-radius: 10px;
    background: linear-gradient(180deg, #d4d6d9 0%, var(--frame-silver) 50%, #8f9296 100%);
    box-shadow: 0 2px 6px rgba(0,0,0,0.35);
  }
  .video-screen {
    left: 130px; top: 172px; width: 360px; height: 219px;
    background: var(--screen-white); border-radius: 8px;
  }
  .video-play { left: 236px; top: 208px; }
  .video-caption { left: 120px; top: 394px; width: 382px; text-align: center; font-size: 18px; color: var(--ink-black); }

  .hero-head { left: 528px; top: 232px; font-size: 34px; font-weight: 700; font-style: italic; color: var(--ink-black); letter-spacing: 0.3px; }
  .hero-sub { left: 528px; top: 272px; font-size: 22px; line-height: 27px; color: var(--ink-grey); }
  .hero-note { left: 528px; top: 355px; font-size: 22px; color: var(--ink-grey); }

  .info-panel {
    left: 108px; top: 455px; width: 983px; height: 257px;
    background: linear-gradient(180deg, #08194d 0%, var(--panel-navy) 100%);
    border-radius: 30px;
  }
  .info-col { top: 487px; width: 240px; }
  .info-col h2 { font-size: 27px; font-weight: 400; margin-bottom: 32px; }
  .info-col p { font-size: 14.5px; line-height: 17.6px; }
  .col-what { left: 140px; }
  .col-who { left: 470px; }
  .col-why { left: 810px; }
  .cta { left: 408px; top: 666px; font-size: 18px; color: var(--link-blue); }

  .site-footer { left: 0; top: 732px; width: 1244px; text-align: center; color: var(--footer-ink); font-size: 13px; line-height: 15.5px; }
  .site-footer a { color: var(--footer-ink); text-decoration: none; }
  .legal-links { margin-bottom: 11px; }
  .legal-links span { margin: 0 6px; }
  .support { margin-top: 15px; }
</style>
</head>
<body>
  <p class="abs tagline">No matter what you sell or what your company size, VIDEO MARKETING is very likely your best opportunity to &nbsp;dramatically increase online sales this year:</p>

  <div class="abs brand">
    <span class="brand-dot"></span>
    <span class="brand-name">Clip Harbor Partners</span>
  </div>

  <nav class="abs main-nav">
    <a class="nav-btn" href="#"><svg width="36" height="28" viewBox="0 0 36 28"><polygon points="2,2 34,14 2,26" fill="#2456d8"/></svg>Home</a>
    <a class="nav-btn" href="#"><svg width="36" height="28" viewBox="0 0 36 28"><polygon points="2,2 34,14 2,26" fill="#2456d8"/></svg>Services</a>
    <a class="nav-btn" href="#"><svg width="36" height="28" viewBox="0 0 36 28"><polygon points="2,2 34,14 2,26" fill="#2456d8"/></svg>Examples</a>
    <a class="nav-btn" href="#"><svg width="36" height="28" viewBox="0 0 36 28"><polygon points="2,2 34,14 2,26" fill="#2456d8"/></svg>Order</a>
    <a class="nav-btn" href="#"><svg width="36" height="28" viewBox="0 0 36 28"><polygon points="2,2 34,14 2,26" fill="#2456d8"/></svg>Contact Us</a>
  </nav>

  <div class="abs hero-panel"></div>
  <svg class="abs hero-curl" width="48" height="46" viewBox="0 0 48 46"><path d="M0,46 C20,40 30,30 34,0 L48,0 L48,10 C46,30 34,42 0,46 Z" fill="#1d7fe0"/></svg>

  <div class="abs video-frame"></div>
  <div class="abs video-screen"></div>
  <svg class="abs video-play" width="148" height="148" viewBox="0 0 148 148">
    <circle cx="74" cy="74" r="71" fill="none" stroke="#fbf59c" stroke-width="5"/>
    <polygon points="46,35 124,74 46,113" fill="#fbf59c"/>
  </svg>
  <p class="abs video-caption">Put Your Video Thumbnail &nbsp;Here.</p>

  <h1 class="abs hero-head">“FIRST PAGE VIDEO LISTINGS</h1>
  <p class="abs hero-sub">on Zentrova for the Keywords of Your Choice...<br>For More Traffic, Leads, and Sales to Your Site!"</p>
  <p class="abs hero-note">We Do It All For You.</p>

  <section class="abs info-panel"></section>
  <div class="abs info-col col-what">
    <h2>What is it?</h2>
    <p>harborclipreach.example will assure you to get first page Zentrova video listings or you get your money back! &nbsp;We work with ALL types of products and services at reasonable rates..</p>
  </div>
  <div class="abs info-col col-who">
    <h2>Who is it for?</h2>
    <p>We help entrepreneurs, small businesses, and even large brands (affiliate marketers too)...</p>
  </div>
  <div class="abs info-col col-why">
    <h2>Why use it?</h2>
    <p>VIDEO is Fast Becoming THE Preferred Method to Expand Your TRAFFIC and SALES on the Internet.</p>
  </div>
  <a class="abs cta" href="#">Get your no-risk video strategy session now!</a>

  <footer class="abs site-footer">
    <p class="legal-links"><a href="#">Disclaimer and TOU</a><span>|</span><a href="#">Privacy</a><span>|</span><a href="#">Disclosure</a><span>&nbsp;|</span><a href="#">Legal</a></p>
    <p>© Plumfield Reels, LLC. - All Rights Reserved</p>
    <p>Trademarks on this page are the property of their respective owners.</p>
    <p class="support">SUPPORT</p>
    <p>800-555-0147</p>
    <p>support@HarborClipReach.example</p>
    <p>www.Korvendesk.example</p>
  </footer>
</body>
</html>
```